Bakery Business Cards

We are in need of business cards for our bakery business--something non-generic that reflects our business and will stand out. We are a wholesale bakery that primarily services in-store bakeries, casinos, schools, distributors, and fund-raising companies. The family business was founded in 1960. (www.marlowsovenworks.com)

```html
<!DOCTYPE html>
<html lang="en">
<head>
<meta charset="utf-8">
<title>Marlow's Oven Works — Business Card</title>
<link href="https://fonts.googleapis.com/css2?family=Libre+Baskerville:wght@400;700&display=swap" rel="stylesheet">
<style>
  :root {
    --backdrop: #a6a6a6;
    --brand-blue: #0047b9;
    --card-ink: #eef2fb;
    --table-wood: #c9995f;
    --wood-light: #dcbb8c;
    --plate-white: #ece6dc;
  }
  html, body {
    margin: 0;
    padding: 0;
    width: 1200px;
    height: 1000px;
    overflow: hidden;
    background: var(--backdrop);
  }
  .canvas {
    position: relative;
    width: 1200px;
    height: 1000px;
    background: var(--backdrop);
  }
  .card {
    position: absolute;
    left: 294px;
    width: 613px;
    height: 351px;
    border-radius: 22px;
    overflow: hidden;
  }
  .card-front {
    top: 93px;
    background: var(--brand-blue);
    color: var(--card-ink);
    font-family: "Libre Baskerville", Georgia, serif;
  }
  .brand {
    position: absolute;
    left: 0;
    right: 0;
    top: 74px;
    text-align: center;
  }
  .brand-name {
    margin: 0;
    font-weight: 700;
  }
  .brand-name-top {
    display: block;
    font-size: 36px;
    line-height: 44px;
    letter-spacing: 1px;
  }
  .brand-name-main {
    display: block;
    font-size: 58px;
    line-height: 72px;
  }
  .brand-since {
    margin: 10px 0 0;
    font-size: 20px;
    line-height: 24px;
    font-weight: 700;
    letter-spacing: 1px;
  }
  .contact {
    position: absolute;
    left: 0;
    right: 0;
    top: 289px;
    margin: 0;
    text-align: center;
    font-size: 14px;
    line-height: 20px;
  }
  .card-back {
    top: 547px;
  }
  .pie-spread {
    width: 100%;
    height: 100%;
    background: linear-gradient(135deg, var(--table-wood) 0%, var(--wood-light) 40%, var(--plate-white) 60%, var(--wood-light) 80%, var(--table-wood) 100%);
  }
</style>
</head>
<body>
<main class="canvas">
  <section class="card card-front">
    <div class="brand">
      <p class="brand-name">
        <span class="brand-name-top">Marlow's</span>
        <span class="brand-name-main">Oven Works</span>
      </p>
      <p class="brand-since">SINCE 1960</p>
    </div>
    <p class="contact">
      (405) 555-0148 · sales@marlowsovenworks.com · www.marlowsovenworks.com<br>
      1375 Linden Row, Fairhaven, OK 73119
    </p>
  </section>
  <section class="card card-back">
    <div class="pie-spread" role="img" aria-label="Overhead photo of pie slices and fruit cobblers on white plates and bowls with forks on a wooden table"></div>
  </section>
</main>
</body>
</html>
```